Tilbury Pane Works Business Card

We need a business card design that is suitable for a Glazing Business. We Specialize in Repairing broken windows and doors and are a 24hr on call service. We manufacture Shower screens, Fly screens, Wardrobe doors, Security doors and grilles + mirrors. We stock a variety of mesh including Standard mesh, Pet resistant mesh, Fendrix & Clearvane. We would like to use a combination of Light Blue, Dark Blue, Black & White with perhaps a picture of glass breaking.

Industry/Entity Type

Business

Contact Information for Business Card

Kelvale Glass Service60B Glasshouse Rocks RdNarooma NSW 2546PH / FAX - 02 44765210MOB - 0417386052 Andrewemail - tilburypane@mailvex.com

Font styles to use
Serif

Colors
34a7d8
0255a3
ffffff

Requirements
Must have
• logo with picture of broken or cracked glass

```html
<!DOCTYPE html>
<html lang="en">
<head>
<meta charset="utf-8">
<title>Tilbury Pane Works – Business Card</title>
<link rel="stylesheet" href="https://fonts.googleapis.com/css2?family=Libre+Baskerville:wght@400;700&family=Noto+Serif:wght@400&display=swap">
<style>
  :root {
    --backdrop: #5e4a36;
    --card-white: #ffffff;
    --ink: #111111;
    --navy: #2b3990;
    --logo-blue: #3a4aa0;
    --band: #8080c0;
    --rule: #222222;
    --glass-black: #050505;
    --glass-grey: #4a4a4a;
  }
  * { box-sizing: border-box; margin: 0; padding: 0; }
  html, body {
    width: 1000px; height: 1200px; overflow: hidden;
    background: var(--backdrop);
  }
  .canvas { position: relative; width: 1000px; height: 1200px; }
  .card {
    position: absolute; left: 92px; width: 806px; height: 497px;
    box-shadow: 0 4px 14px rgba(0,0,0,.45);
    overflow: hidden;
  }
  .card--front { top: 88px; background: var(--card-white); }
  .card--back { top: 625px; background: var(--glass-black); }

  .brand {
    position: absolute; left: 64px; top: 92px;
    display: flex; align-items: center; gap: 14px;
  }
  .brand__mark { width: 34px; height: 34px; background: var(--logo-blue); }
  .brand__name {
    font-family: "Libre Baskerville", serif; font-weight: 400;
    font-size: 29px; letter-spacing: 1px; color: var(--logo-blue);
    text-transform: uppercase; white-space: nowrap;
  }

  .person { position: absolute; left: 56px; top: 251px; }
  .person__name { font-family: "Noto Serif", serif; font-size: 25px; color: var(--ink); line-height: 1.2; }
  .person__title { font-family: "Noto Serif", serif; font-size: 17px; color: var(--navy); line-height: 1.2; margin-top: 2px; }
  .rule { position: absolute; left: 56px; right: 46px; top: 309px; border-top: 1.5px solid var(--rule); }

  .address {
    position: absolute; left: 56px; top: 319px; font-style: normal;
    font-family: "Libre Baskerville", serif; font-size: 17px; line-height: 26px; color: var(--ink);
  }
  .contacts {
    position: absolute; left: 394px; top: 319px; list-style: none;
    font-family: "Libre Baskerville", serif; font-size: 17.5px; line-height: 26px; color: var(--ink);
    white-space: nowrap;
  }
  .contacts li { display: flex; align-items: center; gap: 7px; }
  .contacts svg { width: 19px; height: 19px; flex: none; }

  .tagline {
    position: absolute; left: 0; right: 0; top: 443px; height: 37px;
    background: var(--band); color: var(--card-white);
    font-family: "Libre Baskerville", serif; font-size: 18px;
    display: flex; align-items: center; justify-content: center;
    white-space: nowrap;
  }

  .shattered-glass {
    position: absolute; inset: 0;
    background:
      radial-gradient(ellipse 260px 340px at 40px 110px, rgba(200,200,200,.55), transparent 70%),
      radial-gradient(ellipse 500px 260px at 430px 130px, rgba(90,90,90,.35), transparent 75%),
      linear-gradient(135deg, var(--glass-grey) 0%, var(--glass-black) 45%, var(--glass-black) 100%);
  }
  .services {
    position: absolute; left: 405px; top: 206px;
    font-family: "Libre Baskerville", serif; color: var(--card-white);
  }
  .services__heading { font-size: 17px; font-weight: 700; line-height: 24px; }
  .services__list { list-style: none; font-size: 17px; line-height: 23.5px; margin-bottom: 24px; }
  .services__list li::before {
    content: ""; display: inline-block; width: 10px; height: 10px;
    background: var(--card-white); margin-right: 6px; vertical-align: 1px;
  }
</style>
</head>
<body>
<div class="canvas">
  <section class="card card--front">
    <div class="brand">
      <span class="brand__mark"></span>
      <span class="brand__name">Tilbury Pane Works</span>
    </div>

    <div class="person">
      <p class="person__name">Your name here</p>
      <p class="person__title">Title here</p>
    </div>
    <div class="rule"></div>

    <address class="address">
      17C Marlowe Creek Rd,Kelvale<br>NSW 2581
    </address>

    <ul class="contacts">
      <li>
        <svg viewBox="0 0 20 20"><circle cx="10" cy="10" r="8.5" fill="none" stroke="#2b3990" stroke-width="1.6"/><path d="M6.5 6c.5-.6 1.2-.6 1.6 0l.8 1.4c.2.4 0 .8-.3 1.1l-.4.4c.6 1.3 1.6 2.3 2.9 2.9l.4-.4c.3-.3.7-.5 1.1-.3l1.4.8c.6.4.6 1.1 0 1.6-.8.8-1.8 1-2.8.5A9 9 0 0 1 6 8.8c-.5-1-.3-2 .5-2.8z" fill="#2b3990"/></svg>
        PH / FAX - 02 48193627
      </li>
      <li>
        <svg viewBox="0 0 20 20"><circle cx="10" cy="10" r="8.5" fill="none" stroke="#2b3990" stroke-width="1.6"/><rect x="7" y="5" width="6" height="10" rx="1" fill="none" stroke="#2b3990" stroke-width="1.4"/><circle cx="10" cy="13.2" r=".7" fill="#2b3990"/></svg>
        0417386052
      </li>
      <li>
        <svg viewBox="0 0 20 20"><circle cx="10" cy="10" r="9.2" fill="#2b3990"/><rect x="5.5" y="7" width="9" height="6.2" fill="#fff"/><path d="M5.5 7l4.5 3.5L14.5 7" fill="none" stroke="#2b3990" stroke-width="1"/></svg>
        Colinemail-tilburypane@mailvex.com
      </li>
    </ul>

    <p class="tagline">Repairing broken windows and doors and area 24hr on call service.</p>
  </section>

  <section class="card card--back">
    <div class="shattered-glass" role="img" aria-label="Photograph of shattered glass with white cracks radiating across a black background"></div>
    <div class="services">
      <h3 class="services__heading">WE MANUFACTURE</h3>
      <ul class="services__list">
        <li>Shower screens</li>
        <li>Fly screens</li>
        <li>Wardrobe doors</li>
        <li>Security doors and grilles + mirrors.</li>
      </ul>
      <h3 class="services__heading">WE STOCK A</h3>
      <ul class="services__list">
        <li>variety of mesh including Standard mesh</li>
        <li>Pet resistant mesh</li>
        <li>Fendrix Clearvane</li>
      </ul>
    </div>
  </section>
</div>
</body>
</html>
```